3 out of 100 people will get deadly skin cancer - we need a great illustration that shows this!

We put together a prototype image that communicates lifetime skin cancer risk. (see attached). We are looking for illustrators who can take make a new/better/cooler graphic that communicates this idea. It could be as simple as a superior illustration of the graphic we have or illustrators can propose a completely different idea.What should the illustration communicate?U.S. adults have a lifetime risk of developing skin cancer of 1 in 5. But we don't want to show 1 in 5; we want to show that number in a larger group. For example, in the attached illustration we show 20 in 100 people get skin cancer (i.e., 100 beach towels/umbrellas and 20 of them are red). Research has shown that people are more likely to accurately understand numbers like this when you convey them for larger groups (i.e., 20 out of 100 rather than 1 out of 5). U.S. adults also have a lifetime risk of 2.3% of developing the deadliest form of skin cancer (melanoma). In other words, approximately 3 in 100 people will develop melanoma in their lifetime. Ideally, a single image will convey both lifetime skin cancer risk (20 in 100) and melanoma risk (3 in 100). We will award a top three as follows: 1st place = $300, 2nd place = $250, third place = $200. We will also buy any design beyond 3rd place that we like for $100. For example, we purchased 24 designs in our last contest on Artmarketly.This research is supported by funding from the Corvane Institute of Science.

Target Market(s)

The U.S. public; individuals at high risk of developing skin cancer

Industry/Entity Type

Medicine

Colors

Designer to choose colors to be used in the design.

Requirements
Must have
• an original illustration that conveys both lifetime risk of developing skin cancer (20 in 100) and melanoma (3 in 100).
Nice to have
• It can be beach towels and umbrellas, just like our prototype, or the designers can pitch an original idea. Imagery can be realistic or cartoonish (or something in between). It should be illustrations, though. Not edited photos. The image should be in color (no black and white illustrations).
Should not have
• Photos. Clip art. Free vector images.
• We are looking for original illustrations created by the designer.

```html
<!DOCTYPE html>
<html lang="en">
<head>
<meta charset="utf-8">
<title>For Every 100 People – Skin Cancer Risk</title>
<link rel="stylesheet" href="https://fonts.googleapis.com/css2?family=Archivo:wght@800&display=swap">
<style>
  :root {
    --bg: #ffffff;
    --ring-band: #f9cf66;
    --sun: #f7bc37;
    --sun-map: #f2a51e;
    --person: #f08a24;
    --melanoma: #662483;
    --skin-cancer: #cc1237;
    --ink: #111111;
  }
  html, body {
    margin: 0;
    padding: 0;
    width: 1200px;
    height: 1003px;
    overflow: hidden;
    background: var(--bg);
  }
  .risk-graphic {
    display: block;
    width: 1200px;
    height: 1003px;
  }
  .ring-band { fill: none; stroke: var(--ring-band); stroke-width: 17; }
  .person { fill: var(--person); }
  .person.melanoma { fill: var(--melanoma); }
  .person.skin-cancer { fill: var(--skin-cancer); }
  .sun-disc { fill: var(--sun); }
  .us-map-area { fill: var(--sun-map); }
  .stat-text {
    font-family: "Archivo", "Arial Black", sans-serif;
    font-weight: 800;
  }
  .headline { fill: var(--ink); font-size: 40px; letter-spacing: 1px; }
  .headline-number { fill: var(--ink); font-size: 88px; letter-spacing: -2px; }
  .skin-number { fill: var(--skin-cancer); font-size: 86px; letter-spacing: -2px; }
  .skin-label { fill: var(--skin-cancer); font-size: 30px; }
  .melanoma-number { fill: var(--melanoma); font-size: 86px; }
  .melanoma-label { fill: var(--melanoma); font-size: 30px; }
</style>
</head>
<body>
<svg class="risk-graphic" viewBox="0 0 1200 1003" xmlns="http://www.w3.org/2000/svg">
  <g transform="translate(607 499)">
    <circle class="ring-band" r="436"/>
    <circle class="ring-band" r="365"/>

    <g class="people-outer-ring" role="img" aria-label="Outer ring of 40 people, 10 of whom will develop melanoma">
      <circle class="person" transform="rotate(0)" cy="-436" r="30"/>
      <circle class="person" transform="rotate(9)" cy="-436" r="30"/>
      <circle class="person" transform="rotate(18)" cy="-436" r="30"/>
      <circle class="person" transform="rotate(27)" cy="-436" r="30"/>
      <circle class="person melanoma" transform="rotate(36)" cy="-436" r="30"/>
      <circle class="person" transform="rotate(45)" cy="-436" r="30"/>
      <circle class="person" transform="rotate(54)" cy="-436" r="30"/>
      <circle class="person melanoma" transform="rotate(63)" cy="-436" r="30"/>
      <circle class="person" transform="rotate(72)" cy="-436" r="30"/>
      <circle class="person" transform="rotate(81)" cy="-436" r="30"/>
      <circle class="person" transform="rotate(90)" cy="-436" r="30"/>
      <circle class="person melanoma" transform="rotate(99)" cy="-436" r="30"/>
      <circle class="person" transform="rotate(108)" cy="-436" r="30"/>
      <circle class="person" transform="rotate(117)" cy="-436" r="30"/>
      <circle class="person" transform="rotate(126)" cy="-436" r="30"/>
      <circle class="person" transform="rotate(135)" cy="-436" r="30"/>
      <circle class="person" transform="rotate(144)" cy="-436" r="30"/>
      <circle class="person" transform="rotate(153)" cy="-436" r="30"/>
      <circle class="person melanoma" transform="rotate(162)" cy="-436" r="30"/>
      <circle class="person" transform="rotate(171)" cy="-436" r="30"/>
      <circle class="person" transform="rotate(180)" cy="-436" r="30"/>
      <circle class="person melanoma" transform="rotate(189)" cy="-436" r="30"/>
      <circle class="person" transform="rotate(198)" cy="-436" r="30"/>
      <circle class="person" transform="rotate(207)" cy="-436" r="30"/>
      <circle class="person melanoma" transform="rotate(216)" cy="-436" r="30"/>
      <circle class="person" transform="rotate(225)" cy="-436" r="30"/>
      <circle class="person melanoma" transform="rotate(234)" cy="-436" r="30"/>
      <circle class="person" transform="rotate(243)" cy="-436" r="30"/>
      <circle class="person melanoma" transform="rotate(252)" cy="-436" r="30"/>
      <circle class="person" transform="rotate(261)" cy="-436" r="30"/>
      <circle class="person" transform="rotate(270)" cy="-436" r="30"/>
      <circle class="person" transform="rotate(279)" cy="-436" r="30"/>
      <circle class="person" transform="rotate(288)" cy="-436" r="30"/>
      <circle class="person melanoma" transform="rotate(297)" cy="-436" r="30"/>
      <circle class="person" transform="rotate(306)" cy="-436" r="30"/>
      <circle class="person" transform="rotate(315)" cy="-436" r="30"/>
      <circle class="person" transform="rotate(324)" cy="-436" r="30"/>
      <circle class="person" transform="rotate(333)" cy="-436" r="30"/>
      <circle class="person melanoma" transform="rotate(342)" cy="-436" r="30"/>
      <circle class="person" transform="rotate(351)" cy="-436" r="30"/>
    </g>

    <g class="people-middle-ring" role="img" aria-label="Middle ring of 32 people, 5 with melanoma and 2 with skin cancer">
      <circle class="person melanoma" transform="rotate(5.625)" cy="-365" r="29"/>
      <circle class="person" transform="rotate(16.875)" cy="-365" r="29"/>
      <circle class="person" transform="rotate(28.125)" cy="-365" r="29"/>
      <circle class="person skin-cancer" transform="rotate(39.375)" cy="-365" r="29"/>
      <circle class="person" transform="rotate(50.625)" cy="-365" r="29"/>
      <circle class="person" transform="rotate(61.875)" cy="-365" r="29"/>
      <circle class="person" transform="rotate(73.125)" cy="-365" r="29"/>
      <circle class="person" transform="rotate(84.375)" cy="-365" r="29"/>
      <circle class="person" transform="rotate(95.625)" cy="-365" r="29"/>
      <circle class="person" transform="rotate(106.875)" cy="-365" r="29"/>
      <circle class="person melanoma" transform="rotate(118.125)" cy="-365" r="29"/>
      <circle class="person" transform="rotate(129.375)" cy="-365" r="29"/>
      <circle class="person melanoma" transform="rotate(140.625)" cy="-365" r="29"/>
      <circle class="person" transform="rotate(151.875)" cy="-365" r="29"/>
      <circle class="person" transform="rotate(163.125)" cy="-365" r="29"/>
      <circle class="person" transform="rotate(174.375)" cy="-365" r="29"/>
      <circle class="person" transform="rotate(185.625)" cy="-365" r="29"/>
      <circle class="person melanoma" transform="rotate(196.875)" cy="-365" r="29"/>
      <circle class="person" transform="rotate(208.125)" cy="-365" r="29"/>
      <circle class="person skin-cancer" transform="rotate(219.375)" cy="-365" r="29"/>
      <circle class="person" transform="rotate(230.625)" cy="-365" r="29"/>
      <circle class="person" transform="rotate(241.875)" cy="-365" r="29"/>
      <circle class="person" transform="rotate(253.125)" cy="-365" r="29"/>
      <circle class="person" transform="rotate(264.375)" cy="-365" r="29"/>
      <circle class="person" transform="rotate(275.625)" cy="-365" r="29"/>
      <circle class="person" transform="rotate(286.875)" cy="-365" r="29"/>
      <circle class="person" transform="rotate(298.125)" cy="-365" r="29"/>
      <circle class="person" transform="rotate(309.375)" cy="-365" r="29"/>
      <circle class="person" transform="rotate(320.625)" cy="-365" r="29"/>
      <circle class="person" transform="rotate(331.875)" cy="-365" r="29"/>
      <circle class="person" transform="rotate(343.125)" cy="-365" r="29"/>
      <circle class="person melanoma" transform="rotate(354.375)" cy="-365" r="29"/>
    </g>

    <g class="people-inner-ring" role="img" aria-label="Inner ring of 28 people, 5 with melanoma and 1 with skin cancer">
      <circle class="person" transform="rotate(0)" cy="-297" r="29"/>
      <circle class="person" transform="rotate(12.857)" cy="-297" r="29"/>
      <circle class="person" transform="rotate(25.714)" cy="-297" r="29"/>
      <circle class="person melanoma" transform="rotate(38.571)" cy="-297" r="29"/>
      <circle class="person" transform="rotate(51.429)" cy="-297" r="29"/>
      <circle class="person" transform="rotate(64.286)" cy="-297" r="29"/>
      <circle class="person melanoma" transform="rotate(77.143)" cy="-297" r="29"/>
      <circle class="person" transform="rotate(90)" cy="-297" r="29"/>
      <circle class="person" transform="rotate(102.857)" cy="-297" r="29"/>
      <circle class="person" transform="rotate(115.714)" cy="-297" r="29"/>
      <circle class="person" transform="rotate(128.571)" cy="-297" r="29"/>
      <circle class="person" transform="rotate(141.429)" cy="-297" r="29"/>
      <circle class="person" transform="rotate(154.286)" cy="-297" r="29"/>
      <circle class="person melanoma" transform="rotate(167.143)" cy="-297" r="29"/>
      <circle class="person" transform="rotate(180)" cy="-297" r="29"/>
      <circle class="person" transform="rotate(192.857)" cy="-297" r="29"/>
      <circle class="person" transform="rotate(205.714)" cy="-297" r="29"/>
      <circle class="person" transform="rotate(218.571)" cy="-297" r="29"/>
      <circle class="person" transform="rotate(231.429)" cy="-297" r="29"/>
      <circle class="person melanoma" transform="rotate(244.286)" cy="-297" r="29"/>
      <circle class="person" transform="rotate(257.143)" cy="-297" r="29"/>
      <circle class="person" transform="rotate(270)" cy="-297" r="29"/>
      <circle class="person" transform="rotate(282.857)" cy="-297" r="29"/>
      <circle class="person skin-cancer" transform="rotate(295.714)" cy="-297" r="29"/>
      <circle class="person" transform="rotate(308.571)" cy="-297" r="29"/>
      <circle class="person melanoma" transform="rotate(321.429)" cy="-297" r="29"/>
      <circle class="person" transform="rotate(334.286)" cy="-297" r="29"/>
      <circle class="person" transform="rotate(347.143)" cy="-297" r="29"/>
    </g>

    <circle class="sun-disc" r="235"/>
  </g>

  <rect class="us-map-area" x="394" y="388" width="423" height="257" rx="40"
        role="img" aria-label="Map of the contiguous United States"/>

  <g class="stat-text">
    <text class="headline" x="607" y="343" text-anchor="middle">FOR EVERY</text>
    <text class="headline-number" x="607" y="424" text-anchor="middle">100</text>
    <text class="headline" x="607" y="469" text-anchor="middle">PEOPLE</text>

    <text class="skin-number" x="484" y="563" text-anchor="middle">20</text>
    <text class="skin-label" x="657" y="525" text-anchor="middle">WILL DEVELOP</text>
    <text class="skin-label" x="657" y="563" text-anchor="middle">SKIN CANCER</text>

    <text class="melanoma-number" x="484" y="656" text-anchor="middle">3</text>
    <text class="melanoma-label" x="634" y="620" text-anchor="middle">WILL DEVELOP</text>
    <text class="melanoma-label" x="634" y="658" text-anchor="middle">MELANOMA</text>
  </g>
</svg>
</body>
</html>
```